Theatre Company needs poster for a Christmas show.

We need a poster for an annual Christmas musical show call "A Plum Hush". The style is Jazzy/Lounge Christmas songs. The poster should be a mid-centry modern, Gilt Row-style design. I have attached the past year's poster for reference. The poster should include "VelNOVA Professional Series presents A Plum Hush" the date "December 18th, 2015" our phone number "512-555-0148 ext 207" and our website "vel-nova.org". The poster should also include the logos of our title sponsors (attached).

Target Market(s)

Lakeway, Texas residents, Adults, 21+

Industry/Entity Type

It Company

Font styles to use
Sans Serif

Requirements
Must have
• VelNOVA logo
• Show title "A Plum Hush"
• Date: December 18th, 2015
• Phone number: 512-555-0148 ext 207
• Web site: vel-nova.org
• Sponsor logos at the bottom (attached)
• Mid-century modern, Gilt Row-style design
• Christmas/Winter colors
Nice to have
• Singer/piano/microphone imagery
• cocktail imagery

```html
<!DOCTYPE html>
<html lang="en">
<head>
<meta charset="utf-8">
<title>A Plum Hush — VelNOVA Professional Series</title>
<link rel="stylesheet" href="https://fonts.googleapis.com/css2?family=Rye&family=Oswald:wght@500;600&display=swap">
<style>
  :root {
    --sky-light: #d3eef1;
    --sky: #b7dfe6;
    --sky-deep: #a3d2dc;
    --pine: #7c9f5b;
    --pine-dark: #6a8c4c;
    --ribbon: #ecdcd2;
    --ribbon-shade: #cdb8ad;
    --ink-green: #3e5a35;
    --snow: #ffffff;
    --bar: #2f4a2a;
  }
  * { margin: 0; padding: 0; box-sizing: border-box; }
  html, body { width: 800px; height: 1200px; overflow: hidden; }
  body { background: var(--snow); }

  .poster {
    position: relative;
    width: 800px;
    height: 1200px;
    overflow: hidden;
    background: radial-gradient(ellipse at 50% 40%, var(--sky-light) 0%, var(--sky) 55%, var(--sky-deep) 100%);
    font-family: "Rye", Georgia, serif;
    color: var(--ink-green);
  }

  .tree-art {
    position: absolute;
    left: 90px;
    top: 40px;
    width: 620px;
    height: 980px;
    border-radius: 48% 48% 14% 14% / 70% 70% 8% 8%;
    background: radial-gradient(ellipse at 50% 35%, var(--pine) 0%, var(--pine) 55%, var(--pine-dark) 100%);
  }

  .ribbon {
    position: absolute;
    display: flex;
    align-items: center;
    justify-content: center;
    background: var(--ribbon);
    box-shadow: 0 4px 0 var(--ribbon-shade);
    white-space: nowrap;
  }
  .ribbon--brand   { left: 290px; top: 240px; width: 260px; height: 54px; font-size: 30px; transform: rotate(-8deg); }
  .ribbon--series  { left: 215px; top: 400px; width: 390px; height: 54px; font-size: 25px; transform: rotate(-10deg); }
  .ribbon--title   { left: 190px; top: 532px; width: 470px; height: 78px; font-size: 46px; letter-spacing: 5px; transform: rotate(-8deg); }
  .ribbon--date    { left: 168px; top: 700px; width: 515px; height: 64px; font-size: 34px; transform: rotate(-8deg); }

  .ground {
    position: absolute;
    left: 0;
    bottom: 0;
    width: 800px;
    height: 210px;
  }

  .contact {
    position: absolute;
    left: 0;
    width: 800px;
    top: 1062px;
    display: flex;
    flex-direction: column;
    align-items: center;
    gap: 8px;
    font-family: "Oswald", Arial, sans-serif;
    font-weight: 600;
    color: var(--snow);
  }
  .contact__line {
    background: var(--bar);
    padding: 1px 26px;
    font-size: 24px;
    letter-spacing: 2px;
    line-height: 30px;
  }
  .contact__line--phone { font-size: 20px; line-height: 26px; padding: 0 30px; }

  .sponsors {
    position: absolute;
    left: 60px;
    right: 60px;
    top: 1148px;
    display: flex;
    justify-content: space-between;
    align-items: center;
    font-family: "Oswald", Arial, sans-serif;
    font-weight: 500;
    font-size: 17px;
    color: var(--ink-green);
  }
  .sponsor { display: flex; align-items: center; gap: 6px; }
  .sponsor__mark { width: 12px; height: 12px; border-radius: 50%; background: var(--sky-deep); }
</style>
</head>
<body>
  <main class="poster">
    <div class="tree-art" role="img" aria-label="Stylised green Christmas tree with trunk"></div>

    <div class="ribbon ribbon--brand">VelNOVA</div>
    <div class="ribbon ribbon--series">Professional Series presents</div>
    <h1 class="ribbon ribbon--title">A PLUM HUSH</h1>
    <div class="ribbon ribbon--date">December 18, 2015</div>

    <svg class="ground" viewBox="0 0 800 210" preserveAspectRatio="none" aria-hidden="true">
      <path d="M0 60 Q400 -10 800 60 L800 210 L0 210 Z" fill="#ffffff"/>
    </svg>

    <div class="contact">
      <div class="contact__line">WWW.VEL-NOVA.ORG</div>
      <div class="contact__line contact__line--phone">512.555.0148 EXT 207</div>
    </div>

    <footer class="sponsors">
      <span class="sponsor"><span class="sponsor__mark"></span>VelNOVA</span>
      <span class="sponsor">Harlow &amp; Pine</span>
      <span class="sponsor">Eastwick</span>
      <span class="sponsor"><span class="sponsor__mark"></span>Brightstep</span>
      <span class="sponsor">Corvale</span>
    </footer>
  </main>
</body>
</html>
```